Business card

We are looking for a creative person to deigns our company business card.

Target Market(s)

College age student

Industry/Entity Type

Accommodation

Contact Information for Business Card

We want a fun, clean and sophisticated design. It should look good, but more importantly the information should be legible.

Font styles to use
Serif
Sans Serif
Other font styles liked:
• Open Sans ,

Colors
33a6d7

Requirements
Must have
• Must have a young and memorable message. Be legible.
• Our logo on the back on a solid blue , please find color and logo attached
• LodgeBridgely.net on the back.
Nice to have
• I would like to have couple of different fonts on the LodgeBridgely.net on the back of the cards with a solid blue.

```html
<!DOCTYPE html>
<html lang="en">
<head>
<meta charset="utf-8">
<title>LodgeBridgely – Business Card</title>
<link rel="stylesheet" href="https://fonts.googleapis.com/css2?family=Open+Sans:wght@600;700;800&display=swap">
<style>
  :root {
    --stage: #1a1b1b;
    --brand-blue: #33a6d7;
    --pattern-blue: #3399d6;
    --navy: #0e4f7e;
    --ink-grey: #4a4a4a;
    --card-white: #ffffff;
  }
  * { margin: 0; padding: 0; box-sizing: border-box; }
  html, body {
    width: 1200px; height: 1000px; overflow: hidden;
    background: var(--stage);
    font-family: "Open Sans", Arial, sans-serif;
  }
  .card {
    position: absolute;
    left: 270px;
    width: 660px; height: 377px;
    border-radius: 22px;
    overflow: hidden;
  }
  /* Back side */
  .card-back { top: 70px; background: var(--pattern-blue); }
  .back-pattern {
    position: absolute; inset: 0;
    background: linear-gradient(135deg, #3aa0dc 0%, var(--pattern-blue) 50%, #2f8fcc 100%);
  }
  .back-badge {
    position: absolute; left: 50%; top: 50%;
    width: 290px; height: 290px; margin: -145px 0 0 -145px;
    border-radius: 50%;
    background: var(--card-white);
    box-shadow: 0 10px 18px rgba(0,0,0,0.22);
    display: flex; align-items: center; justify-content: center;
  }
  .brand-name {
    font-weight: 800; color: var(--navy);
    letter-spacing: -0.5px;
  }
  .back-badge .brand-name { font-size: 34px; }

  /* Front side */
  .card-front { top: 533px; background: var(--card-white); }
  .name-block {
    position: absolute; left: 34px; top: 30px;
    padding-left: 24px;
    border-left: 8px solid var(--brand-blue);
  }
  .person-name {
    font-size: 34px; font-weight: 800; color: var(--navy);
    line-height: 1.05; letter-spacing: 0.5px;
  }
  .person-title {
    font-size: 16px; font-weight: 700; color: var(--ink-grey);
  }
  .address {
    position: absolute; left: 40px; top: 140px;
    font-size: 17px; font-weight: 700; color: var(--ink-grey);
    line-height: 1.55;
  }
  .front-brand {
    position: absolute; right: 44px; top: 110px;
    display: flex; flex-direction: column; align-items: center; gap: 14px;
  }
  .front-brand .brand-dot {
    width: 84px; height: 84px; border-radius: 50%;
    background: var(--brand-blue);
  }
  .front-brand .brand-name { font-size: 30px; }
  .contact-row {
    position: absolute; left: 40px; right: 40px; bottom: 32px;
    display: flex; justify-content: space-between; align-items: flex-end;
  }
  .contact-item {
    display: flex; flex-direction: column; align-items: center; gap: 8px;
    font-size: 16px; font-weight: 700; color: var(--ink-grey);
  }
  .contact-item svg { width: 20px; height: 20px; fill: var(--navy); }
</style>
</head>
<body>

<section class="card card-back" aria-label="Card back">
  <div class="back-pattern" role="img" aria-label="Repeating blue house-shape pattern"></div>
  <div class="back-badge">
    <span class="brand-name">LodgeBridgely</span>
  </div>
</section>

<section class="card card-front" aria-label="Card front">
  <div class="name-block">
    <div class="person-name">JOHN DOE</div>
    <div class="person-title">Manager</div>
  </div>

  <address class="address" style="font-style: normal;">
    318 Marlowe St.,<br>
    Suite 207. Portland, Oregon OR 97205
  </address>

  <div class="front-brand">
    <div class="brand-dot"></div>
    <span class="brand-name">LodgeBridgely</span>
  </div>

  <div class="contact-row">
    <div class="contact-item">
      <svg viewBox="0 0 24 24" aria-hidden="true"><path d="M2 5h20v14H2z M2 5l10 8 10-8" fill="none" stroke="#0e4f7e" stroke-width="0"/><path d="M2 5h20l-10 8z M2 7l10 8 10-8v12H2z"/></svg>
      <span>email@LodgeBridgely.net</span>
    </div>
    <div class="contact-item">
      <svg viewBox="0 0 24 24" aria-hidden="true"><path d="M7 2l3 5-2 2c1 3 3 5 6 6l2-2 5 3-2 5C10 21 3 14 2 5z"/></svg>
      <span>014.552.0193</span>
    </div>
    <div class="contact-item">
      <svg viewBox="0 0 24 24" aria-hidden="true" fill="none"><g fill="none" stroke="#0e4f7e" stroke-width="2"><circle cx="12" cy="12" r="9"/><ellipse cx="12" cy="12" rx="4" ry="9"/><path d="M3 12h18M5 7h14M5 17h14"/></g></svg>
      <span>www.LodgeBridgely.net</span>
    </div>
  </div>
</section>

</body>
</html>
```